Hold Each Morning As A MOSSbright Harbour

Hello Designers! We need a captivating notebook cover design for our self-development company for people with disabilities. We help people with a diagnosis see everyday as a MOSSbright Harbour than something to ensure. This notebook is to capture the brightness and positivity of everyday, that your struggles are meant for you to overcome. We would like to see designs that follow with our brand (uploaded) and I've also added our logo and kind of notebook as a guide. The final design should be inviting and bright. Use the title "Keep Each Morning A Quiet Lantern". Will decide the words once the background design is finalized

Notebook Size: 8.5 x 5.75 inches
Updates

Hello Designers! I'm extending the deadline to give you an opportunity to submit different and unique designs for the MOSSbright HARBOUR Journal. I've given feedback to most of you so this is your opportunity to try something new. Looking for clean, inviting and unique designs that use the logo colour scheme (attached -- navy blue, light blue, yellow, black). Preferably front and back cover designs.

Target Market(s)

Between 25-35 years

Font styles to use
Serif
Sans Serif
Decorative
Script

Colors
0255a3
fbed22

Requirements
Must have
• -Use colour scheme as per attachment as main colours (can go beyond for contrast ex. pinks/purples/indigo/etc)
Nice to have
• Would like to see designs related to nature, art and/or graphic prints.
Should not have
• icons (no stick figures), silhouettes of people, no hands
• NO stock images

```html
<!DOCTYPE html>
<html lang="en">
<head>
<meta charset="utf-8">
<title>MOSSbright Harbour Journal – Front and Back Cover</title>
<link href="https://fonts.googleapis.com/css2?family=Kaushan+Script&display=swap" rel="stylesheet">
<style>
  :root {
    --backdrop: #8c8c8c;
    --navy: #1c2a66;
    --sky: #9fc3e3;
    --white: #ffffff;
    --ink: #0a0d18;
    --sun: #ecc51a;
    --night: #0b0612;
    --plum: #4b1a4a;
    --glow: #f3e9b8;
  }
  * { box-sizing: border-box; margin: 0; padding: 0; }
  html, body {
    width: 1200px; height: 1200px; overflow: hidden;
    background: var(--backdrop);
  }
  .spread { position: relative; width: 1200px; height: 1200px; }
  .cover {
    position: absolute; top: 282px; width: 500px; height: 678px; overflow: hidden;
  }
  .cover--front { left: 68px; background: var(--night); }
  .cover--back { left: 632px; }

  .front-art {
    position: absolute; inset: 0;
    background:
      radial-gradient(ellipse 120px 55px at 230px 520px, var(--glow) 0%, #e58ab0 45%, rgba(140,40,120,0) 100%),
      radial-gradient(ellipse 260px 200px at 150px 420px, rgba(70,50,160,0.75) 0%, rgba(70,50,160,0) 100%),
      radial-gradient(ellipse 260px 180px at 170px 40px, rgba(190,60,130,0.8) 0%, rgba(190,60,130,0) 100%),
      radial-gradient(ellipse 240px 200px at 470px 40px, rgba(150,70,30,0.85) 0%, rgba(150,70,30,0) 100%),
      linear-gradient(180deg, var(--plum) 0%, #2a1030 40%, var(--night) 75%);
  }
  .cover-title {
    position: absolute; left: 90px; top: 110px; width: 320px;
    font-family: "Kaushan Script", cursive; font-weight: 400; color: var(--white);
    text-align: center; transform: rotate(-8deg); line-height: 1;
  }
  .cover-title__lead { display: block; font-size: 64px; }
  .cover-title__mid { display: block; font-size: 34px; margin-top: 4px; }
  .cover-title__main { display: block; font-size: 58px; margin-top: 2px; }

  .back-art {
    position: absolute; inset: 0;
    background: linear-gradient(172deg,
      var(--navy) 0%, var(--navy) 26%,
      var(--sky) 36%, var(--sun) 48%,
      var(--sun) 88%, var(--navy) 100%);
  }

  .brand {
    position: absolute; text-align: center;
    font-family: "Kaushan Script", cursive; font-weight: 400; line-height: 1;
  }
  .brand__name { display: block; font-size: 32px; }
  .brand__tag { display: block; font-size: 10px; letter-spacing: 0.5px; margin-top: 12px; }
  .brand--light { left: 150px; top: 596px; width: 180px; color: var(--white); }
  .brand--dark { left: 155px; top: 496px; width: 190px; color: var(--ink); }
  .brand--dark .brand__name { font-size: 40px; }
  .brand--dark .brand__tag { font-size: 11px; margin-top: 14px; }
</style>
</head>
<body>
<main class="spread">
  <section class="cover cover--front">
    <div class="front-art" role="img" aria-label="Starry night-sky nebula in magenta, violet and amber with a glowing light cloud near the bottom"></div>
    <h1 class="cover-title">
      <span class="cover-title__lead">Keep Each</span>
      <span class="cover-title__mid">Morning A Quiet</span>
      <span class="cover-title__main">Lantern</span>
    </h1>
    <div class="brand brand--light">
      <span class="brand__name">Ellery's</span>
      <span class="brand__tag">MOSSbright Harbour</span>
    </div>
  </section>

  <section class="cover cover--back">
    <div class="back-art" role="img" aria-label="Graphic print in navy, light blue and yellow for the back cover"></div>
    <div class="brand brand--dark">
      <span class="brand__name">Ellery's</span>
      <span class="brand__tag">MOSSbright Harbour</span>
    </div>
  </section>
</main>
</body>
</html>
```